PowerPoint Template

We would like new powerpoint template for our organization: Fjordvik Data Guild.
Enclosed you find our logo and old template.
Industry/Entity Type
Computer
Requirements
Must have
- 1. Logo
2. Footer (for autor)
3. Font: Variations of ARIAL

```html
<!DOCTYPE html>
<html lang="no">
<head>
<meta charset="utf-8">
<title>Hva gjør vi? – Fjordvik Data Guild</title>
<link rel="stylesheet" href="https://fonts.googleapis.com/css2?family=Arimo:wght@400;700&display=swap">
<style>
  :root {
    --slide-bg-top: #e8f3fb;
    --slide-bg-bottom: #ffffff;
    --wave-light: #cfe9f8;
    --wave-mid: #9fd3f1;
    --wave-deep: #5bb5e6;
    --title-blue: #2f8fd6;
    --title-shadow: rgba(40, 70, 110, 0.35);
    --bullet-text: #3a5cc4;
    --bullet-dot: #3ec7dc;
    --brand-text: #333333;
    --brand-mark: #e8414d;
    --url-text: #111111;
  }
  * { margin: 0; padding: 0; box-sizing: border-box; }
  html, body { width: 1200px; height: 896px; overflow: hidden; }
  body { font-family: "Arimo", Arial, sans-serif; background: #ffffff; }

  .slide {
    position: relative;
    width: 1200px;
    height: 896px;
    overflow: hidden;
    background: linear-gradient(180deg, var(--slide-bg-top) 0%, #f4f9fd 35%, var(--slide-bg-bottom) 70%);
  }
  .slide__waves {
    position: absolute;
    top: 0; left: 0;
    width: 1200px; height: 150px;
  }
  .slide__title {
    position: absolute;
    left: 100px; top: 112px;
    font-size: 64px;
    font-weight: 700;
    color: var(--title-blue);
    text-shadow: 3px 3px 4px var(--title-shadow);
    letter-spacing: 0.5px;
  }
  .slide__bullets {
    position: absolute;
    left: 132px; top: 276px;
    list-style: none;
  }
  .slide__bullets li {
    position: relative;
    padding-left: 30px;
    font-size: 37px;
    font-weight: 700;
    line-height: 68px;
    color: var(--bullet-text);
  }
  .slide__bullets li::before {
    content: "";
    position: absolute;
    left: 2px; top: 28px;
    width: 13px; height: 13px;
    border-radius: 50%;
    background: var(--bullet-dot);
  }
  .brand {
    position: absolute;
    left: 824px; top: 599px;
    width: 376px; height: 297px;
    background: #ffffff;
    display: flex;
    flex-direction: column;
    align-items: center;
    justify-content: center;
    gap: 26px;
  }
  .brand__name {
    display: flex;
    align-items: center;
    gap: 16px;
    font-size: 30px;
    font-weight: 700;
    color: var(--brand-text);
  }
  .brand__square {
    width: 40px; height: 40px;
    background: var(--brand-mark);
  }
  .brand__url {
    font-size: 28px;
    font-weight: 400;
    color: var(--url-text);
  }
</style>
</head>
<body>
  <main class="slide">
    <svg class="slide__waves" viewBox="0 0 1200 150" preserveAspectRatio="none" aria-hidden="true">
      <path d="M0 0 H1200 V40 C1000 110 760 20 520 70 C330 110 150 60 0 95 Z" fill="var(--wave-light)"/>
      <path d="M0 0 H1200 V20 C980 80 760 10 540 45 C340 78 160 35 0 65 Z" fill="var(--wave-mid)" opacity="0.8"/>
      <path d="M0 0 H1200 V8 C1000 50 780 0 560 22 C360 45 170 15 0 38 Z" fill="var(--wave-deep)" opacity="0.7"/>
    </svg>

    <h1 class="slide__title">Hva gjør vi?</h1>

    <ul class="slide__bullets">
      <li>Markedsfører arrangementer</li>
      <li>Bidrar til å verve medlemmer</li>
      <li>Skaper synlighet i Sosiale Medier</li>
      <li>Bygger merkevare og FDGs omdømme</li>
    </ul>

    <div class="brand">
      <div class="brand__name"><span class="brand__square"></span>Fjordvik Data Guild</div>
      <div class="brand__url">fjordvikdata.no</div>
    </div>
  </main>
</body>
</html>
```